Harborline Restoration Business Card Design Phase 2

Professional and clean design. The design colors should flow with the logo. Two-sided card with the website on the back which is:

www.HarborlineRestoration.example.

"Specializing in Water Damage Restoration"

On the front I need the name, email, phone, and logo.

Name: Darnell Vickery
Email: Darnell@HarborlineRestoration.example
Phone: 555-018-2734 for now

I only have the Preview and Thumbnail right now but should have the source files uploaded within a day or two.

Target Market(s)

Flood victims, home owners with water damage from busted pipes etc...

Industry/Entity Type

Business

Contact Information for Business Card

Name: Darnell Vickery

Font styles to use
Serif
Sans Serif

Requirements
Must have
• Business Card Details Info

```html
<!DOCTYPE html>
<html lang="en">
<head>
<meta charset="utf-8">
<title>Harborline Restoration Business Card</title>
<link href="https://fonts.googleapis.com/css2?family=Oswald:wght@700&family=Exo+2:wght@400;500&family=Libre+Baskerville:ital,wght@1,700&display=swap" rel="stylesheet">
<style>
  :root {
    --green: #4a9440;
    --green-dark: #3d8a42;
    --navy: #1d3a63;
    --teal-navy: #173d5e;
    --white: #ffffff;
    --rule: #8a94a3;
    --backdrop: #e9e7e3;
  }
  * { margin: 0; padding: 0; box-sizing: border-box; }
  html, body { width: 1200px; height: 952px; overflow: hidden; }
  body {
    background: var(--backdrop);
    position: relative;
    font-family: "Exo 2", sans-serif;
  }
  .card {
    position: absolute;
    left: 290px;
    width: 620px;
    height: 355px;
    overflow: hidden;
    box-shadow: 0 6px 18px rgba(0,0,0,0.18);
  }
  .card-back { top: 91px; background: linear-gradient(180deg, var(--green-dark) 0%, var(--teal-navy) 78%); }
  .card-front { top: 506px; background: var(--white); }
  .card svg.bands { position: absolute; inset: 0; width: 100%; height: 100%; }
  .wordmark {
    position: absolute;
    left: 0; right: 0;
    text-align: center;
    font-family: "Oswald", sans-serif;
    font-weight: 700;
    text-transform: uppercase;
    line-height: 0.95;
    letter-spacing: 0.5px;
  }
  .card-back .wordmark { top: 48px; font-size: 74px; color: var(--white); }
  .card-front .wordmark { top: 30px; font-size: 52px; color: var(--navy); }
  .tagline {
    position: absolute;
    top: 230px; left: 0; right: 0;
    text-align: center;
    font-family: "Libre Baskerville", serif;
    font-style: italic;
    font-weight: 700;
    font-size: 15px;
    color: var(--white);
  }
  .website {
    position: absolute;
    right: 34px; top: 318px;
    font-size: 15px;
    color: var(--white);
    letter-spacing: 0.3px;
    white-space: nowrap;
  }
  .divider {
    position: absolute;
    left: 36px; right: 36px; top: 196px;
    height: 2px; background: var(--rule);
  }
  .person {
    position: absolute;
    left: 40px; top: 218px;
    display: flex; align-items: center; gap: 14px;
  }
  .person-name { font-size: 22px; font-weight: 500; color: var(--green); white-space: nowrap; }
  .contact {
    position: absolute;
    left: 300px; right: 20px; top: 222px;
    display: flex; flex-direction: column; gap: 6px;
  }
  .contact-row { display: flex; align-items: center; gap: 10px; font-size: 14px; color: var(--navy); white-space: nowrap; }
</style>
</head>
<body>

<section class="card card-back" aria-label="Card back">
  <svg class="bands" viewBox="0 0 620 355" aria-hidden="true">
    <polygon points="0,312 285,312 270,355 0,355" fill="var(--green)"/>
    <polygon points="300,300 620,300 620,355 280,355" fill="var(--green)"/>
  </svg>
  <div class="wordmark">Harborline<br>Restoration</div>
  <p class="tagline">"Specializing in Water Damage Restoration"</p>
  <p class="website">www.HarborlineRestoration.example</p>
</section>

<section class="card card-front" aria-label="Card front">
  <svg class="bands" viewBox="0 0 620 355" aria-hidden="true">
    <polygon points="440,0 620,0 620,20 425,20" fill="var(--navy)"/>
    <polygon points="0,300 300,300 285,345 0,335" fill="var(--navy)"/>
    <polygon points="310,298 620,305 620,355 270,355" fill="var(--green)"/>
  </svg>
  <div class="wordmark">Harborline<br>Restoration</div>
  <div class="divider"></div>
  <div class="person">
    <svg width="26" height="26" viewBox="0 0 26 26" aria-hidden="true">
      <circle cx="13" cy="13" r="13" fill="var(--navy)"/>
      <circle cx="13" cy="10" r="4" fill="var(--white)"/>
      <path d="M6 20 q7 -9 14 0 z" fill="var(--white)"/>
    </svg>
    <span class="person-name">Darnell Vickery</span>
  </div>
  <div class="contact">
    <div class="contact-row">
      <svg width="14" height="14" viewBox="0 0 14 14" aria-hidden="true">
        <circle cx="7" cy="7" r="7" fill="var(--green)"/>
        <path d="M4.5 3.5 l1.5 0 0.6 2 -0.9 0.8 q0.8 1.6 2 2 l0.8 -0.9 2 0.6 0 1.5 q-4.5 0.5 -6 -6 z" fill="var(--white)"/>
      </svg>
      <span>555-018-2734</span>
    </div>
    <div class="contact-row">
      <svg width="14" height="11" viewBox="0 0 14 11" aria-hidden="true">
        <rect width="14" height="11" fill="var(--green)"/>
        <path d="M0 0 L7 6 L14 0" fill="none" stroke="var(--white)" stroke-width="1.2"/>
      </svg>
      <span>Darnell@HarborlineRestoration.example</span>
    </div>
  </div>
</section>

</body>
</html>
```